kestrova business cards

Hey design gurus!
I'm after a clean, modern, stylish business card for my about to be launched company.
I've uploaded the logos for my company "Kestrova Electrical Solutions"
and also the tarrow alliance logo to whom i am associated.

```html
<!DOCTYPE html>
<html lang="en">
<head>
<meta charset="utf-8">
<title>Kestrova Electrical Solutions – Business Card</title>
<link href="https://fonts.googleapis.com/css2?family=Montserrat:wght@400;500;700;800&display=swap" rel="stylesheet">
<style>
  :root{
    --backdrop:#4a4a4a;
    --card-navy:#0a161e;
    --back-navy:#0d1c26;
    --back-navy-deep:#08131a;
    --brand-blue:#1f8fd2;
    --ink-white:#ffffff;
    --ink-soft:#e9eef2;
  }
  *{margin:0;padding:0;box-sizing:border-box}
  html,body{width:1200px;height:801px;overflow:hidden;background:var(--backdrop)}
  .stage{width:1200px;height:801px;display:flex;flex-direction:column;align-items:center;justify-content:center;gap:22px}
  .card{position:relative;width:648px;height:370px;border-radius:18px;overflow:hidden;box-shadow:0 14px 32px rgba(0,0,0,.35)}
  .card-front{background:var(--card-navy);font-family:'Montserrat',sans-serif;color:var(--ink-white)}
  .card-back{background:linear-gradient(135deg,var(--back-navy),var(--back-navy-deep))}
  .card-wave{position:absolute;inset:0;width:100%;height:100%}

  .brand-lockup{position:absolute;left:60px;top:68px;display:flex;align-items:center;gap:12px}
  .brand-dot{width:36px;height:36px;border-radius:50%;background:var(--brand-blue);flex:none}
  .brand-name{font-weight:700;color:var(--brand-blue);text-transform:uppercase;line-height:1}
  .brand-name .brand-main{display:block;font-size:28px;letter-spacing:1px}
  .brand-name .brand-sub{display:block;font-size:9.5px;letter-spacing:2.2px;margin-top:4px}

  .partner-badge{position:absolute;left:60px;top:148px;width:230px;height:100px}

  .divider{position:absolute;left:328px;top:58px;width:1.5px;height:190px;background:var(--brand-blue)}

  .contact-block{position:absolute;left:348px;top:48px}
  .person-name{font-weight:800;font-size:22px;color:var(--brand-blue);letter-spacing:1px;text-transform:uppercase;line-height:1.2}
  .person-role{font-weight:400;font-size:15px;color:var(--ink-soft);line-height:1.3}
  .address{font-size:14px;color:var(--ink-soft);margin-top:14px;line-height:1.35}
  .contact-list{list-style:none;margin-top:12px}
  .contact-list li{display:flex;align-items:center;gap:9px;font-size:14px;color:var(--ink-soft);line-height:1.5}
  .contact-icon{width:12px;height:12px;flex:none}
</style>
</head>
<body>
<main class="stage">
  <section class="card card-front">
    <svg class="card-wave" viewBox="0 0 648 370" preserveAspectRatio="none" aria-hidden="true">
      <path d="M0,370 C190,366 340,335 445,282 C535,236 595,222 648,214 L648,370 Z" fill="var(--brand-blue)"/>
      <path d="M0,366 C185,360 330,325 432,270 C525,220 590,204 648,196 L648,204 C592,212 532,228 440,278 C338,330 190,364 0,372 Z" fill="var(--ink-white)"/>
    </svg>

    <div class="brand-lockup">
      <span class="brand-dot"></span>
      <span class="brand-name"><span class="brand-main">Kestrova</span><span class="brand-sub">Electrical Solutions</span></span>
    </div>

    <svg class="partner-badge" viewBox="0 0 230 100" role="img" aria-label="Tarrow Alliance partner badge">
      <rect x="1.5" y="1.5" width="227" height="97" rx="12" fill="none" stroke="var(--ink-white)" stroke-width="2"/>
      <rect x="16" y="24" width="52" height="52" rx="6" fill="var(--ink-white)"/>
    </svg>

    <div class="divider"></div>

    <div class="contact-block">
      <h1 class="person-name">Dorian Pell</h1>
      <p class="person-role">Managing Director</p>
      <p class="address">Your address, City<br>State, Zip 1234</p>
      <ul class="contact-list">
        <li>
          <svg class="contact-icon" viewBox="0 0 24 24"><path d="M6.6 10.8a15 15 0 0 0 6.6 6.6l2.2-2.2a1 1 0 0 1 1-.25 11.4 11.4 0 0 0 3.6.57 1 1 0 0 1 1 1V20a1 1 0 0 1-1 1A17 17 0 0 1 3 4a1 1 0 0 1 1-1h3.5a1 1 0 0 1 1 1c0 1.25.2 2.45.57 3.57a1 1 0 0 1-.25 1z" fill="var(--brand-blue)"/></svg>
          555 014 2278
        </li>
        <li>
          <svg class="contact-icon" viewBox="0 0 24 24"><path d="M2 5h20v14H2z" fill="var(--brand-blue)"/><path d="M2 5l10 8 10-8" fill="none" stroke="var(--card-navy)" stroke-width="2"/></svg>
          hello@kestrova.com
        </li>
        <li>
          <svg class="contact-icon" viewBox="0 0 24 24"><circle cx="12" cy="12" r="10" fill="var(--brand-blue)"/><path d="M2 12h20M12 2c3 3 3 17 0 20M12 2c-3 3-3 17 0 20" fill="none" stroke="var(--card-navy)" stroke-width="1.5"/></svg>
          www.kestrova.com
        </li>
      </ul>
    </div>
  </section>

  <section class="card card-back" role="img" aria-label="Card back: repeating embossed company monogram pattern on dark navy"></section>
</main>
</body>
</html>
```